Invitation to Retail Shopping Event

-Must include logo
-Can contain product pictures depending on design
-I prefer any graphics to be my own product pictures
-Should include the following language:
Sip and Shop
Thursday, November 18
11 to 1 pm
478 Fenwick Lane
Come enjoy sips, snacks and shopping! Be the first to preview our new winter collection and get an early start on your holiday gifting.
Please RSVP to 402-319-5577 or info@pelbrika.com

```html
<!DOCTYPE html>
<html lang="en">
<head>
<meta charset="utf-8">
<title>Sip &amp; Shop Invitation – Pelbrika</title>
<link rel="stylesheet" href="https://fonts.googleapis.com/css2?family=Great+Vibes&family=Questrial&family=Montserrat:wght@500&display=swap">
<style>
  :root {
    --page-top: #ffffff;
    --page-bottom: #d9d9d9;
    --gold-edge: #d3ac57;
    --gold-light: #f9f4a1;
    --navy: #262a35;
    --copper: #b0672e;
    --ink: #7a4433;
    --pill: #a06a50;
    --pill-text: #f4d9d2;
    --white: #ffffff;
  }
  * { margin: 0; padding: 0; box-sizing: border-box; }
  html, body { width: 1200px; height: 1200px; overflow: hidden; }
  body {
    position: relative;
    background: linear-gradient(180deg, var(--page-top) 0%, var(--page-bottom) 100%);
    font-family: "Questrial", "Helvetica Neue", Arial, sans-serif;
    color: var(--ink);
  }
  .invitation {
    position: absolute;
    left: 186px; top: 0;
    width: 828px; height: 1200px;
    background: linear-gradient(180deg, var(--gold-edge) 0%, var(--gold-light) 47%, var(--gold-edge) 100%);
    box-shadow: 4px 0 10px rgba(0,0,0,0.18);
  }
  .side-band {
    position: absolute; top: 0; height: 1200px;
    background: var(--navy);
  }
  .side-band--left { left: 24px; width: 80px; }
  .side-band--right { left: 738px; width: 65px; }
  .pinstripe {
    position: absolute; top: 0; height: 1200px; width: 2px;
    background: var(--copper);
  }
  .pinstripe--left { left: 42px; }
  .pinstripe--right { left: 784px; }

  .centered { position: absolute; left: 0; width: 828px; text-align: center; }

  .brand {
    position: absolute; left: 288px; top: 92px; width: 252px;
    text-align: center;
    color: var(--white);
    font-size: 40px; letter-spacing: 3px;
    line-height: 48px;
  }
  .title {
    top: 196px;
    font-family: "Great Vibes", cursive;
    font-size: 118px; line-height: 140px;
  }
  .date-row { position: absolute; top: 358px; left: 0; width: 828px; height: 70px; }
  .date-month, .date-year { position: absolute; top: 22px; font-size: 21px; }
  .date-month { left: 250px; }
  .date-year { left: 530px; }
  .date-day { position: absolute; left: 363px; width: 139px; text-align: center; }
  .date-weekday { font-size: 22px; line-height: 28px; display: block; }
  .date-number { font-size: 36px; line-height: 36px; display: block; }
  .date-rule { position: absolute; top: 18px; width: 2px; height: 38px; background: var(--ink); }
  .date-rule--a { left: 362px; }
  .date-rule--b { left: 501px; }

  .time-pill {
    position: absolute; left: 320px; top: 462px;
    width: 188px; height: 45px;
    background: var(--pill);
    border-radius: 22px 0 22px 0;
    color: var(--pill-text);
    font-family: "Montserrat", Arial, sans-serif; font-weight: 500;
    font-size: 24px; letter-spacing: 3px; line-height: 45px;
    text-align: center;
  }
  .address { top: 552px; font-size: 26px; }
  .welcome { top: 624px; font-size: 30px; line-height: 39px; }
  .divider { position: absolute; left: 294px; top: 734px; width: 240px; height: 4px; }
  .details { top: 786px; font-size: 22px; line-height: 30px; }
  .rsvp { top: 892px; font-size: 24px; line-height: 32px; }
  .rsvp-or { top: 962px; font-size: 21px; }
  .rsvp-email { top: 1006px; font-size: 24px; }
  .flourish {
    position: absolute; left: 206px; top: 1100px; width: 416px; height: 32px;
    background: linear-gradient(90deg, rgba(122,68,51,0) 0%, rgba(122,68,51,0.35) 50%, rgba(122,68,51,0) 100%);
  }
</style>
</head>
<body>
  <main class="invitation">
    <div class="side-band side-band--left"></div>
    <div class="pinstripe pinstripe--left"></div>
    <div class="side-band side-band--right"></div>
    <div class="pinstripe pinstripe--right"></div>

    <div class="brand">PELBRIKA</div>

    <h1 class="centered title">Sip &amp; Shop</h1>

    <div class="date-row">
      <span class="date-month">November</span>
      <span class="date-rule date-rule--a"></span>
      <span class="date-day">
        <span class="date-weekday">Thursday</span>
        <span class="date-number">18</span>
      </span>
      <span class="date-rule date-rule--b"></span>
      <span class="date-year">2021</span>
    </div>

    <div class="time-pill">11 to 1 pm</div>

    <p class="centered address">478 Fenwick Lane</p>

    <p class="centered welcome">Come enjoy sips,<br>snacks and shopping !</p>

    <svg class="divider" viewBox="0 0 240 4" aria-hidden="true">
      <rect x="0" y="1.5" width="240" height="1" fill="#7a4433"/>
    </svg>

    <p class="centered details">Be the first to preview our new winter collection<br>and get an early start on your holiday gifting.</p>

    <p class="centered rsvp">Please RSVP to<br>402-319-5577</p>
    <p class="centered rsvp-or">or</p>
    <p class="centered rsvp-email">info@pelbrika.com</p>

    <div class="flourish" role="img" aria-label="Decorative scroll flourish border"></div>
  </main>
</body>
</html>
```